日焼け止めスティックの容器デザインを募集いたします。

パッケージデザインコンペの際はたくさんのご応募誠にありがとうございました。
今回は容器のデザインを募集いたします。

■商品名:Pearl Day Veil+

■容器に必ず入れていただきたいもの(①~⑦)
=表=
①商品名:PEARL DAY VEIL+(Pearl Day Veil+でも可)
※商品名は現状仮のため、ご修正いただく可能性がございます

②ブランド名:MORVICADE

③ブランドロゴ
aiデータにしてお渡しいたします。
選定させていただいた方にお送りいたしますので
仮で「logo」の記載をお願いします。

④補足成分:CLOUD KEEP ORBICINE(Cloud Keep Orbicineでも可)

⑤クラウドキープオルビシンマーク ※添付画像1

⑥日焼け防止効果指数:SPF50+/PA++++

⑦英語での商品説明
Beautiful at any moment.
Portable UV protector
containing Cloud Keep Orbicine

⑧容量:20g

=裏=
⑨裏面の記載事項(成分表示等)
裏面に関しましては、選定させていただきました方のみにお送りいたします。
ご調整いただきながらご対応をいただけますと幸いです。

■パッケージ仕様とデザイン要件に関しまして
スティック容器:幅50mm×高さ100mm(手持ち部分も含む) ※画像添付
デザイン範囲:幅26mmm×高さ65mm 特色4色+白
※デザインしていただくのは、スティックの蓋の部分になります。
デザイン:ベースはネイビーのグラデーションにてお願いします ※画像添付
横でのデザイン・縦でのデザインの複数デザインをいただきたいです。
箔押し:ブランドロゴ部分はホットスタンプ刻印です。
---
※容器の実物は添付PDFをご覧ください

■ターゲット
20代~30代女性(美容好き、ECモールで買い物をする層)
(例)
・毎日自宅でスキンケアをする都内OL
・美白を意識していて、日焼け止めが欠かせない人
・メイクの上からでもしっかり太陽ダメージから守りたい人

■理想とするデザインの世界観
・PicvoraやNexloに投稿できるような映えるデザイン
・シンプルながらも品よく高級感があり、おしゃれなデザイン
・カバンに入れて持ち運んでいて、使いたくなる、また見られたとしても恥ずかしくないデザイン

■理想と異なるイメージ
・人の顔等を乗せたデザイン
・ガーリーすぎるデザイン(フリフリのレースやリボンなど)
・ドクロなどのデザイン
・ボタニカルすぎるデザイン

■納品までの流れ
①コンペにてデザインを募集、選定(弊社)
②選定したクイロラ様に直接ご連絡(下記クイロラ様)
-デザイン等の微調整依頼
-展開図送付(実際に展開図にデザインを入れていただきます)
-必要の場合は裏面修正
③入稿データに問題がないか確認(弊社)
④問題がなければ校了作業後、納品完了手続き(両者)

※成分表示の確認等を行いながらとなりますので、
ご選定させていただいてから何度か修正をお願いする可能性がございます。
何卒ご了承いただきますようお願いいたします。

■納品形式
ai,psdのいずれかでお願いいたします。
パスがわかれてる状態で納品いただけますと幸いです。

■その他/注意点
・選択させて頂いたデザインの著作権(財産権)等の扱いはQuillora利用規約に従い、弊社に譲渡をお願いします。
・フォントや画像素材などを利用する場合は、上記利用用途に使用できることを確認し、第三者の知的財産権等に注意して下さい。
・印刷サイズ・入稿時の関係で、納品後にも多少修正のご依頼をさせていただく場合がありますので、予めご了承ください。
・採用後に表記内容の修正を依頼する場合がございます。
以下の資料を添付いたします。
1:クラウドキープオルビシンマーク
2:容器参考画像一覧(PDF)
3:容器ベースカラーイメージ図(PDF)
4:デザイン可能範囲(PDF)
仮ロゴマークをお渡しさせていただくのを失念しておりましたので追記いたします。
(こちらのロゴマークは仮になりますので最終デザイン前に差し替えていただきます)
容器イメージを添付いたします。
容器イメージにデザインしていただけましたら幸いです。
容器のイメージ(蓋のグラデーションあり)を添付いたします。
グラデーションは
・黒→白
・濃紺→白
・ネイビー→白
のどれかをイメージしております。

ご確認の程宜しくお願い致します。
樹脂色は指定の紺/黒で作成していただき
印刷部分のデザインをお願いいたします。
ご応募ありがとうございます。
・ロゴマークとMORVICADEは 横並びではなく
離して使用していただいて問題ないです。
(資料添付:ロゴ位置_参考画像)

・デザインのグラデーションに合わせて、容器もグラデーションを
かけていただきますようお願いします。

引き続きよろしくお願いします。
延長いたします。
たくさんのご応募ありがとうございます。
延長をいたします。

ブランドイメージに逸脱せず、高級感のあるデザインに
していただいた為、採用させていただきます

この度は、たくさんのご応募ありがとうございました。
今後、容器のデザイン等で再度ご依頼させていただくかと存じております。
その際は何卒よろしくおねがいいたします。

```html
<!DOCTYPE html>
<html lang="en">
<head>
<meta charset="utf-8">
<title>MORVICADE Pearl Day Veil+ — Stick Cap</title>
<link rel="stylesheet" href="https://fonts.googleapis.com/css2?family=Josefin+Sans:wght@100;200;300;400&display=swap">
<style>
  :root {
    --cap-white: #ffffff;
    --cap-mist: #dcdee6;
    --cap-haze: #9397b2;
    --cap-navy: #2b3163;
    --cap-deep: #161b45;
    --cap-ink: #10143a;
    --brand-ink: #2e3a68;
    --sub-ink: #46528a;
    --spf-ink: #e4e7f2;
    --copy-ink: #3b4a9a;
    --net-ink: #6a74a6;
    --badge-line: #a9b0cf;
    --title-ink: #ffffff;
  }
  html, body {
    margin: 0;
    padding: 0;
    width: 1200px;
    height: 3000px;
    overflow: hidden;
  }
  .stick-cap {
    position: relative;
    width: 1200px;
    height: 3000px;
    overflow: hidden;
    font-family: "Josefin Sans", sans-serif;
    background: linear-gradient(180deg,
      var(--cap-white) 0%,
      var(--cap-white) 5%,
      var(--cap-mist) 12%,
      var(--cap-haze) 22%,
      var(--cap-navy) 34%,
      var(--cap-deep) 70%,
      var(--cap-ink) 100%);
  }
  .brand-mark {
    position: absolute;
    left: 480px;
    top: 80px;
    width: 240px;
    height: 240px;
  }
  .brand-name {
    position: absolute;
    top: 540px;
    left: 0;
    width: 100%;
    text-align: center;
    font-size: 72px;
    font-weight: 400;
    letter-spacing: 8px;
    color: var(--brand-ink);
    margin: 0;
  }
  .ingredient {
    position: absolute;
    left: 170px;
    top: 790px;
    width: 820px;
    margin: 0;
    text-align: center;
    font-weight: 300;
    font-size: 84px;
    line-height: 120px;
  }
  .ingredient span { display: block; white-space: nowrap; }
  .ingredient .ingredient-name { color: var(--sub-ink); }
  .ingredient .spf-rating { color: var(--spf-ink); }
  .ingredient-badge {
    position: absolute;
    left: 970px;
    top: 890px;
    width: 170px;
    height: 170px;
  }
  .product-name {
    position: absolute;
    top: 1130px;
    left: 0;
    width: 100%;
    margin: 0;
    color: var(--title-ink);
    font-weight: 100;
    text-align: center;
    line-height: 1;
  }
  .product-name span { display: block; white-space: nowrap; }
  .product-name .line-one { font-size: 300px; letter-spacing: 4px; }
  .product-name .line-two { font-size: 560px; margin-top: 40px; }
  .product-name .line-three { font-size: 230px; margin-top: 20px; font-weight: 200; }
  .description {
    position: absolute;
    top: 2380px;
    left: 0;
    width: 100%;
    margin: 0;
    text-align: center;
    color: var(--copy-ink);
    font-weight: 300;
    font-size: 60px;
    line-height: 96px;
  }
  .description span { display: block; white-space: nowrap; }
  .net-weight {
    position: absolute;
    top: 2800px;
    left: 0;
    width: 100%;
    margin: 0;
    text-align: center;
    color: var(--net-ink);
    font-weight: 300;
    font-size: 84px;
  }
</style>
</head>
<body>
  <main class="stick-cap">
    <svg class="brand-mark" viewBox="0 0 240 240" role="img" aria-label="MORVICADE brand logo mark (hot-stamped)">
      <circle cx="120" cy="120" r="110" fill="none" stroke="var(--brand-ink)" stroke-width="5"/>
    </svg>
    <p class="brand-name">MORVICADE</p>

    <p class="ingredient">
      <span class="ingredient-name">Cloud Keep Orbicine</span>
      <span class="spf-rating">SPF50+/PA++++</span>
    </p>
    <svg class="ingredient-badge" viewBox="0 0 170 170" role="img" aria-label="Cloud Keep Orbicine ingredient mark">
      <circle cx="85" cy="85" r="79" fill="none" stroke="var(--badge-line)" stroke-width="4"/>
    </svg>

    <h1 class="product-name">
      <span class="line-one">PEARL</span>
      <span class="line-two">DAY</span>
      <span class="line-three">VEIL+</span>
    </h1>

    <p class="description">
      <span>Beautiful at any moment.</span>
      <span>Portable UV protector</span>
      <span>containing Cloud Keep Orbicine</span>
    </p>

    <p class="net-weight">20g</p>
  </main>
</body>
</html>
```